Business Card Design for new social media business

I am looking for a new professional business card design for an exciting new company which is based on providing members with experiences of others to benefit their choice of places to visit for restaurants, bars, clubs, national monument, tourist sights, hotels and so forth.
Updates

Please submit designs as I will choose to commit the funds depending on designs.

Target Market(s)

Business Managers as well as directors alongside owners

Industry/Entity Type

Business

Requirements
Must have
• Logo design and symbols
Nice to have
• Logo / Symbol on the back of the business card and possibly the logo as if embedded/embossed on the business card.

```html
<!DOCTYPE html>
<html lang="en">
<head>
<meta charset="utf-8">
<title>TripVoice Business Card</title>
<link rel="stylesheet" href="https://fonts.googleapis.com/css2?family=Open+Sans:wght@400;600;700&display=swap">
<style>
  :root {
    --canvas: #e9eaec;
    --brand-blue: #3a68b8;
    --brand-orange: #f47b20;
    --ink: #3c3c3c;
    --ink-soft: #555a60;
    --card-white: #ffffff;
    --emboss: #ececec;
    --social: #9aa3ad;
  }
  * { box-sizing: border-box; margin: 0; padding: 0; }
  html, body {
    width: 1200px; height: 900px; overflow: hidden;
    background: var(--canvas);
    font-family: "Open Sans", Arial, sans-serif;
  }
  .canvas {
    position: relative; width: 1200px; height: 900px;
    display: flex; flex-direction: column; align-items: center; justify-content: center; gap: 60px;
  }
  .card {
    position: relative; width: 588px; height: 336px; overflow: hidden;
    border-radius: 4px; box-shadow: 0 6px 18px rgba(0,0,0,.12);
  }
  /* back side */
  .card-back { background: var(--brand-blue); }
  .card-back .brand {
    position: absolute; right: 44px; bottom: 40px;
    display: flex; align-items: center; gap: 12px;
  }
  .card-back .brand-name { color: var(--card-white); font-weight: 700; font-size: 46px; letter-spacing: -1px; }
  .brand-dot { width: 22px; height: 22px; border-radius: 50%; background: var(--brand-orange); }

  /* front side */
  .card-front { background: var(--card-white); }
  .card-front .emboss {
    position: absolute; right: -70px; bottom: -120px;
    width: 330px; height: 330px; border-radius: 50%;
    background: radial-gradient(circle at 40% 35%, #f6f6f6, var(--emboss));
  }
  .card-front .brand {
    position: absolute; left: 40px; top: 34px;
    display: flex; align-items: center; gap: 10px;
  }
  .card-front .brand-name { color: var(--brand-blue); font-weight: 700; font-size: 40px; letter-spacing: -1px; }
  .details { position: absolute; left: 48px; top: 110px; }
  .person-name { font-size: 15px; font-weight: 600; letter-spacing: 1px; color: var(--ink); text-transform: uppercase; }
  .person-role { font-size: 12px; color: var(--brand-orange); margin-bottom: 10px; }
  .contact-list { list-style: none; font-size: 12px; color: var(--ink-soft); }
  .contact-list li { display: flex; align-items: center; gap: 8px; line-height: 20px; }
  .contact-list svg { width: 12px; height: 12px; fill: var(--brand-orange); }
  .address { margin-top: 10px; font-size: 12px; color: var(--ink); }
  .social-row { position: absolute; right: 150px; bottom: 40px; display: flex; gap: 8px; }
  .social-row span { width: 22px; height: 22px; border-radius: 3px; background: var(--social); }
</style>
</head>
<body>
<main class="canvas">
  <section class="card card-back" aria-label="Card back">
    <div class="brand">
      <span class="brand-name">TripVoice</span>
      <span class="brand-dot"></span>
    </div>
  </section>

  <section class="card card-front" aria-label="Card front">
    <div class="emboss"></div>
    <div class="brand">
      <span class="brand-dot"></span>
      <span class="brand-name">TripVoice</span>
    </div>
    <div class="details">
      <p class="person-name">Aren Kole</p>
      <p class="person-role">Managing Director</p>
      <ul class="contact-list">
        <li><svg viewBox="0 0 24 24"><path d="M6.6 10.8a15.1 15.1 0 0 0 6.6 6.6l2.2-2.2a1 1 0 0 1 1-.25 11.4 11.4 0 0 0 3.6.57 1 1 0 0 1 1 1V20a1 1 0 0 1-1 1A17 17 0 0 1 3 4a1 1 0 0 1 1-1h3.5a1 1 0 0 1 1 1c0 1.25.2 2.45.57 3.57a1 1 0 0 1-.25 1z"/></svg>+20 987654321</li>
        <li><svg viewBox="0 0 24 24"><path d="M2 5h20v14H2zm2 2v.5l8 5 8-5V7l-8 5z"/></svg>hello@tripvoice.com</li>
        <li><svg viewBox="0 0 24 24"><path d="M12 2a10 10 0 1 0 0 20 10 10 0 0 0 0-20zm0 2c.9 0 2.2 2.1 2.6 5H9.4C9.8 6.1 11.1 4 12 4zM4.3 11h3a16 16 0 0 0 0 2h-3a8 8 0 0 1 0-2zm5.1 2a14 14 0 0 1 0-2h5.2a14 14 0 0 1 0 2zm7.3 0a16 16 0 0 0 0-2h3a8 8 0 0 1 0 2zM12 20c-.9 0-2.2-2.1-2.6-5h5.2c-.4 2.9-1.7 5-2.6 5z"/></svg>www.tripvoice.com</li>
      </ul>
      <p class="address">42 Harbor Lane, #05-12 Suite B, USA 010014</p>
    </div>
    <div class="social-row" aria-label="Social profiles">
      <span></span><span></span><span></span>
    </div>
  </section>
</main>
</body>
</html>
```